Brochure Design - Non-Profit Fundraising Stream

We are a non-profit organization that is developing a fundraising project through the donation of life insurance policies. We have three brochures in each English and French that we developed for a sister organization that we want to reintegrate with our Foundation, keeping the same copy text just changing the logos, colors and make it overall more visually appealing. The foundation is called the 'Varnek-Holt Syndrome Foundation Canada'.
The original files in .docx format are attached as is the full logo and two symbol files. The deliverables would be six documents in total (InDesign or .docx), each brochure in English and French. The color hex codes are:
red: #7b2850
dark blue: #2c79a7
pale blue: #78b2e2

```html
<!DOCTYPE html>
<html lang="en">
<head>
<meta charset="utf-8">
<title>Unlock the Hidden Value in Your Life Insurance – Varnek-Holt Syndrome Foundation Canada</title>
<link rel="stylesheet" href="https://fonts.googleapis.com/css2?family=Roboto+Condensed:wght@700&family=Montserrat:wght@400;500;600&display=swap">
<style>
  :root{
    --red:#7b2850;
    --red-soft:#b36e8c;
    --dark-blue:#2c79a7;
    --pale-blue:#78b2e2;
    --mist:#eaf3fb;
    --mist-deep:#cfe3f4;
    --ink:#2b2b2b;
    --paper:#ffffff;
  }
  *{margin:0;padding:0;box-sizing:border-box}
  html,body{width:849px;height:1200px;overflow:hidden;background:var(--paper)}
  .brochure{position:relative;width:849px;height:1200px;overflow:hidden;background:var(--paper);font-family:"Montserrat",sans-serif;color:var(--ink)}
  .backdrop{position:absolute;inset:0;width:849px;height:1200px}
  .icon-defs{position:absolute;width:0;height:0}

  .brand{position:absolute;top:66px;left:430px;width:380px;display:flex;align-items:center;gap:16px}
  .brand-mark{flex:none;width:46px;height:46px;border-radius:50%;background:var(--red)}
  .brand-name{font-family:"Montserrat",sans-serif;font-weight:600;font-size:25px;line-height:31px;color:var(--dark-blue)}

  .headline-rule{position:absolute;top:312px;left:40px;width:7px;height:76px;background:var(--red);border-radius:4px}
  .headline{position:absolute;top:307px;left:56px;width:362px;text-align:center;font-family:"Roboto Condensed",sans-serif;font-weight:700;font-size:33px;line-height:41px;color:var(--red)}
  .headline .accent{color:var(--dark-blue)}

  .intro{position:absolute;top:400px;left:61px;width:353px;font-size:15.2px;line-height:18.8px;text-align:justify;color:var(--ink)}

  .section-title{font-family:"Roboto Condensed",sans-serif;font-weight:700;color:var(--red)}
  .policies-title{position:absolute;top:620px;left:61px;font-size:25px}

  .heart-list{list-style:none}
  .heart-list li{position:relative;padding-left:24px}
  .heart-list li svg{position:absolute;left:0;top:3px;width:18px;height:16px}

  .policies{position:absolute;top:659px;left:62px;width:300px;font-weight:500;font-size:15.6px;line-height:19px;color:var(--red)}
  .policies li{margin-bottom:8px}

  .advantages-title{position:absolute;top:907px;left:0;width:849px;text-align:center;font-size:27px}
  .advantages{position:absolute;top:954px;font-size:15.6px;line-height:19px;color:var(--ink)}
  .advantages li{padding-left:29px;margin-bottom:8px}
  .advantages li svg{top:2px}
  .advantages.left{left:62px;width:345px}
  .advantages.right{left:435px;width:340px}
</style>
</head>
<body>
<main class="brochure">
  <svg class="icon-defs" aria-hidden="true">
    <symbol id="heart" viewBox="0 0 18 16"><path d="M9,15 C3,10 0,7 0,4 C0,1.5 2,0 4.2,0 C6.3,0 8,1.5 9,3 C10,1.5 11.7,0 13.8,0 C16,0 18,1.5 18,4 C18,7 15,10 9,15 Z" fill="var(--red)"/></symbol>
  </svg>

  <svg class="backdrop" viewBox="0 0 849 1200" aria-hidden="true">
    <defs>
      <linearGradient id="panelFade" x1="0" y1="0" x2="0" y2="1">
        <stop offset="0" stop-color="#f4f9fd"/>
        <stop offset="1" stop-color="#d6e8f6"/>
      </linearGradient>
      <linearGradient id="blueSweep" x1="0" y1="0" x2="1" y2="1">
        <stop offset="0" stop-color="#78b2e2"/>
        <stop offset="1" stop-color="#2c79a7"/>
      </linearGradient>
    </defs>
    <!-- header band -->
    <rect class="header-band" x="0" y="0" width="849" height="14" fill="var(--dark-blue)"/>
    <rect class="header-accent" x="0" y="14" width="849" height="4" fill="var(--pale-blue)"/>
    <!-- right feature panel -->
    <path class="feature-panel" d="M470,18 L849,18 L849,880 L560,880 Z" fill="url(#panelFade)"/>
    <line class="brand-rule" x1="430" y1="150" x2="810" y2="150" stroke="var(--red)" stroke-width="2"/>
    <!-- circle composition -->
    <circle class="disc-large" cx="700" cy="470" r="170" fill="url(#blueSweep)"/>
    <circle class="disc-inner" cx="700" cy="470" r="105" fill="var(--pale-blue)" opacity=".55"/>
    <circle class="ring" cx="700" cy="470" r="200" fill="none" stroke="var(--red-soft)" stroke-width="3"/>
    <circle class="disc-accent" cx="585" cy="700" r="46" fill="var(--red)"/>
    <circle class="disc-small" cx="790" cy="745" r="28" fill="var(--dark-blue)"/>
    <circle class="dot" cx="520" cy="250" r="12" fill="var(--pale-blue)"/>
    <!-- divider -->
    <rect class="section-divider" x="330" y="888" width="190" height="4" rx="2" fill="var(--pale-blue)"/>
    <!-- footer bands -->
    <path class="footer-red" d="M0,1140 L849,1098 L849,1110 L0,1152 Z" fill="var(--red)"/>
    <path class="footer-dark" d="M0,1152 L849,1110 L849,1200 L0,1200 Z" fill="var(--dark-blue)"/>
    <path class="footer-pale" d="M0,1178 L849,1150 L849,1200 L0,1200 Z" fill="var(--pale-blue)"/>
  </svg>

  <header class="brand">
    <span class="brand-mark"></span>
    <span class="brand-name">Varnek-Holt Syndrome Foundation Canada</span>
  </header>

  <span class="headline-rule" aria-hidden="true"></span>
  <h1 class="headline">Unlock the <span class="accent">HIDDEN VALUE</span><br>In your <span class="accent">LIFE INSURANCE</span></h1>

  <p class="intro">You can maintain or substantially improve your financial position by unlocking the hidden value of your unwanted or unaffordable life insurance via a charitable donation. Every year, seniors over the age of 70 lapse or surrender almost $7 billion of insurance that they might otherwise donate to a charity. You can pay down debt, make major purchases or replenish retirement savings by accessing the value you deserve after paying premiums for decades.</p>

  <h2 class="section-title policies-title">SUITABLE POLICIES</h2>
  <ul class="heart-list policies">
    <li><svg viewBox="0 0 18 16"><use href="#heart"/></svg>Term, Whole life, Universal or term-to-100 policies</li>
    <li><svg viewBox="0 0 18 16"><use href="#heart"/></svg>Insured lives over 70 years old</li>
    <li><svg viewBox="0 0 18 16"><use href="#heart"/></svg>In-force greater than 2 years</li>
    <li><svg viewBox="0 0 18 16"><use href="#heart"/></svg>Minimum death benefit of $50,000</li>
  </ul>

  <h2 class="section-title advantages-title">ADVANTAGES OF DONATING A LIFE INSURANCE POLICY</h2>
  <ul class="heart-list advantages left">
    <li><svg viewBox="0 0 18 16"><use href="#heart"/></svg>You obtain a tax receipt (good for 5 years) for 10%-50% of the face value of the policy (even for term policies that have no “cash surrender value”)</li>
    <li><svg viewBox="0 0 18 16"><use href="#heart"/></svg>You convert a “worthless or low cash value policy” into cash in your pocket when you file your income taxes</li>
  </ul>
  <ul class="heart-list advantages right">
    <li><svg viewBox="0 0 18 16"><use href="#heart"/></svg>Eliminate the burden of annual premium expenses</li>
    <li><svg viewBox="0 0 18 16"><use href="#heart"/></svg>A Foundation becomes the owner and beneficiary, and it funds the premiums and collects the benefit upon maturity</li>
  </ul>
</main>
</body>
</html>
```